Remote Planning & Scheduling Power Point Presentation

This PP presentation is to help explain what RPS is and its benefits. Need help with a better illustration on slide 3 that explains the process, overall aesthetics, need better images, and cleaner workflow on slide 18. Keep the ZOL Logo in the bottom right of each slide. I have included a one-pager and infographic to help. I am still working of verbiage.

Thanks
JR

```html
<!DOCTYPE html>
<html lang="en">
<head>
<meta charset="utf-8">
<title>RPS Flow Process</title>
<link rel="stylesheet" href="https://fonts.googleapis.com/css2?family=Questrial&family=Mulish:wght@600;700;800&display=swap">
<style>
  :root {
    --navy: #0c2f87;
    --navy-deep: #082a7c;
    --slate: #4a525c;
    --slate-light: #5b636d;
    --red: #e8304a;
    --yellow: #f5c40f;
    --sky: #1ea0e0;
    --green: #7ac143;
    --halo: #ffffff;
    --disc: #e6e8ec;
    --fan-back: #d5d9e0;
    --faint: #f1f3f7;
    --mark: #b7c1d7;
    --white: #ffffff;
  }
  html, body {
    margin: 0;
    padding: 0;
    width: 1200px;
    height: 706px;
    overflow: hidden;
    background: var(--white);
  }
  .slide {
    display: block;
    width: 1200px;
    height: 706px;
  }
  .slide-title {
    font-family: "Questrial", "Century Gothic", sans-serif;
    font-size: 48px;
    fill: var(--white);
  }
  .step-label {
    font-family: "Mulish", "Century Gothic", sans-serif;
    font-weight: 700;
    font-size: 14px;
    fill: var(--navy);
  }
  .hub-label {
    font-family: "Mulish", "Century Gothic", sans-serif;
    font-weight: 800;
    font-size: 15px;
    fill: var(--navy);
  }
  .small-hub-label {
    font-family: "Mulish", "Century Gothic", sans-serif;
    font-weight: 700;
    font-size: 9.5px;
    fill: var(--navy);
  }
  .sector-label {
    font-family: "Mulish", "Century Gothic", sans-serif;
    font-weight: 600;
    font-size: 9px;
    fill: var(--white);
  }
  .brand-mark {
    font-family: "Mulish", "Century Gothic", sans-serif;
    font-weight: 800;
    font-size: 30px;
    fill: var(--mark);
  }
  .header-band { fill: var(--navy-deep); }
  .header-slope { fill: var(--slate); }
  .header-peak { fill: var(--slate-light); }
  .bg-peak { fill: var(--faint); }
  .arrow-navy { fill: var(--navy); }
  .arrow-yellow { fill: var(--yellow); }
  .fan-back { fill: var(--fan-back); }
  .sector-core { fill: var(--navy); stroke: var(--white); stroke-width: 2; }
  .sector-red { fill: var(--red); stroke: var(--white); stroke-width: 3; }
  .sector-yellow { fill: var(--yellow); stroke: var(--white); stroke-width: 3; }
  .sector-sky { fill: var(--sky); stroke: var(--white); stroke-width: 3; }
  .sector-green { fill: var(--green); stroke: var(--white); stroke-width: 3; }
  .hub-halo { fill: var(--halo); }
  .hub-disc { fill: var(--disc); }
  .badge-ring { fill: var(--white); stroke: var(--navy); stroke-width: 3; }
  .icon-navy { fill: var(--navy); color: var(--navy); }
  .icon-white { fill: var(--white); color: var(--white); }
  .hex-outline-navy { fill: var(--white); stroke: var(--navy); stroke-width: 2; }
  .hex-fill-navy { fill: var(--navy); }
  .hex-outline-yellow { fill: var(--white); stroke: var(--yellow); stroke-width: 2; }
  .hex-fill-yellow { fill: var(--yellow); }
  .hex-disc { fill: var(--disc); }
</style>
</head>
<body>
<svg class="slide" viewBox="0 0 1300 765" preserveAspectRatio="none" xmlns="http://www.w3.org/2000/svg" role="img" aria-label="RPS flow process diagram">
  <defs>
    <filter id="soft-shadow" x="-20%" y="-20%" width="140%" height="140%">
      <feDropShadow dx="0" dy="2" stdDeviation="3" flood-color="#000" flood-opacity="0.25"/>
    </filter>
    <linearGradient id="header-fade" x1="0" y1="0" x2="0" y2="1">
      <stop offset="0" stop-color="#c9ccd2"/>
      <stop offset="1" stop-color="#ffffff"/>
    </linearGradient>
    <radialGradient id="disc-grad" cx="0.5" cy="0.4" r="0.6">
      <stop offset="0" stop-color="#f4f5f7"/>
      <stop offset="1" stop-color="#dcdfe5"/>
    </radialGradient>

    <symbol id="ico-team" viewBox="0 0 40 28">
      <circle cx="20" cy="7" r="5.5" fill="currentColor"/>
      <path d="M10 27c0-6 4.5-10 10-10s10 4 10 10z" fill="currentColor"/>
      <circle cx="8" cy="10" r="4" fill="currentColor"/>
      <path d="M0 25c0-5 3.5-8 8-8 1.5 0 3 .4 4 1-2 2-3 4.5-3 7z" fill="currentColor"/>
      <circle cx="32" cy="10" r="4" fill="currentColor"/>
      <path d="M40 25c0-5-3.5-8-8-8-1.5 0-3 .4-4 1 2 2 3 4.5 3 7z" fill="currentColor"/>
    </symbol>
    <symbol id="ico-calendar" viewBox="0 0 24 24">
      <g fill="none" stroke="currentColor" stroke-width="1.6">
        <rect x="2.5" y="4" width="19" height="17.5" rx="1"/>
        <line x1="2.5" y1="8.5" x2="21.5" y2="8.5"/>
        <line x1="7" y1="2" x2="7" y2="6"/>
        <line x1="17" y1="2" x2="17" y2="6"/>
        <line x1="7.2" y1="8.5" x2="7.2" y2="21.5"/>
        <line x1="12" y1="8.5" x2="12" y2="21.5"/>
        <line x1="16.8" y1="8.5" x2="16.8" y2="21.5"/>
        <line x1="2.5" y1="13" x2="21.5" y2="13"/>
        <line x1="2.5" y1="17.2" x2="21.5" y2="17.2"/>
      </g>
    </symbol>
    <symbol id="ico-camera" viewBox="0 0 40 30">
      <g fill="none" stroke="currentColor" stroke-width="2.4">
        <path d="M3 8h9l3-5h10l3 5h9v19H3z" stroke-linejoin="round"/>
        <circle cx="20" cy="17" r="7"/>
      </g>
      <rect x="6" y="11" width="4" height="2.5" fill="currentColor"/>
    </symbol>
    <symbol id="ico-list" viewBox="0 0 24 24">
      <g fill="currentColor">
        <circle cx="5" cy="6" r="1.6"/><rect x="8.5" y="5" width="11" height="2" rx="1"/>
        <circle cx="5" cy="12" r="1.6"/><rect x="8.5" y="11" width="11" height="2" rx="1"/>
        <circle cx="5" cy="18" r="1.6"/><rect x="8.5" y="17" width="11" height="2" rx="1"/>
      </g>
    </symbol>
    <symbol id="ico-scope" viewBox="0 0 24 24">
      <g fill="currentColor">
        <circle cx="7" cy="7" r="4.5"/>
        <circle cx="15" cy="15" r="5"/>
        <rect x="9" y="9" width="4" height="4" transform="rotate(45 11 11)"/>
      </g>
    </symbol>
    <symbol id="ico-scroll" viewBox="0 0 24 24">
      <g fill="none" stroke="currentColor" stroke-width="1.8">
        <path d="M6 3h12v15a3 3 0 0 1-3 3H4a2 2 0 0 1 2-2z"/>
        <line x1="9" y1="8" x2="15" y2="8"/>
        <line x1="9" y1="12" x2="15" y2="12"/>
      </g>
    </symbol>
    <symbol id="ico-doc" viewBox="0 0 24 24">
      <g fill="none" stroke="currentColor" stroke-width="1.8">
        <rect x="5" y="3" width="14" height="18" rx="1"/>
        <line x1="8" y1="8" x2="16" y2="8"/>
        <line x1="8" y1="12" x2="16" y2="12"/>
        <line x1="8" y1="16" x2="16" y2="16"/>
      </g>
    </symbol>
    <symbol id="ico-cycle" viewBox="0 0 24 24">
      <g fill="none" stroke="currentColor" stroke-width="1.8">
        <circle cx="12" cy="12" r="6"/>
      </g>
      <g fill="currentColor">
        <circle cx="12" cy="3" r="2"/><circle cx="12" cy="21" r="2"/>
        <circle cx="3" cy="12" r="2"/><circle cx="21" cy="12" r="2"/>
        <circle cx="5.6" cy="5.6" r="1.6"/><circle cx="18.4" cy="18.4" r="1.6"/>
        <circle cx="18.4" cy="5.6" r="1.6"/><circle cx="5.6" cy="18.4" r="1.6"/>
      </g>
    </symbol>
    <symbol id="ico-network" viewBox="0 0 24 24">
      <g fill="none" stroke="currentColor" stroke-width="1.5">
        <line x1="12" y1="12" x2="12" y2="4"/><line x1="12" y1="12" x2="4" y2="9"/>
        <line x1="12" y1="12" x2="20" y2="9"/><line x1="12" y1="12" x2="6" y2="19"/>
        <line x1="12" y1="12" x2="18" y2="19"/>
        <circle cx="12" cy="12" r="3" fill="#fff"/>
        <circle cx="12" cy="4" r="2.2" fill="#fff"/><circle cx="4" cy="9" r="2.2" fill="#fff"/>
        <circle cx="20" cy="9" r="2.2" fill="#fff"/><circle cx="6" cy="19" r="2.2" fill="#fff"/>
        <circle cx="18" cy="19" r="2.2" fill="#fff"/>
      </g>
    </symbol>
    <symbol id="ico-window-search" viewBox="0 0 24 24">
      <g fill="none" stroke="currentColor" stroke-width="1.6">
        <rect x="2" y="3" width="18" height="15" rx="1"/>
        <line x1="2" y1="7" x2="20" y2="7"/>
        <line x1="5" y1="10.5" x2="12" y2="10.5"/>
        <line x1="5" y1="14" x2="10" y2="14"/>
        <circle cx="16" cy="16" r="3.5" fill="#fff"/>
        <line x1="18.5" y1="18.5" x2="22" y2="22"/>
      </g>
    </symbol>
    <symbol id="ico-signal" viewBox="0 0 24 16">
      <g fill="none" stroke="currentColor" stroke-width="1.4">
        <circle cx="12" cy="8" r="2"/>
        <path d="M7.5 3.5a6.5 6.5 0 0 0 0 9"/><path d="M16.5 3.5a6.5 6.5 0 0 1 0 9"/>
        <path d="M4.5 1a10 10 0 0 0 0 14"/><path d="M19.5 1a10 10 0 0 1 0 14"/>
      </g>
    </symbol>
    <symbol id="ico-handshake" viewBox="0 0 48 32">
      <g fill="none" stroke="currentColor" stroke-width="2.6" stroke-linejoin="round" stroke-linecap="round">
        <path d="M2 10l8-5 8 3 6-2 6 3"/>
        <path d="M46 10l-8-5-10 5-6 5 3 2 7-4"/>
        <path d="M10 5v14l10 9c1.5 1.5 3.5 1 4-.5"/>
        <path d="M38 5v14l-8 8"/>
        <path d="M18 23l4 4M22 20l5 5M26 17l5 5"/>
      </g>
    </symbol>
  </defs>

  <!-- background peaks -->
  <g class="backdrop">
    <polygon class="bg-peak" points="1108,258 790,765 1300,765 1300,560"/>
    <polygon class="bg-peak" points="880,470 640,765 1100,765" opacity="0.7"/>
  </g>

  <!-- header -->
  <g class="header">
    <rect x="22" y="220" width="1260" height="14" fill="url(#header-fade)"/>
    <rect class="header-band" x="22" y="22" width="1260" height="198"/>
    <polygon class="header-slope" points="840,220 975,22 1282,22 1282,220"/>
    <polygon class="header-peak" points="1105,28 940,220 1282,220 1282,170"/>
    <text class="slide-title" x="113" y="140">RPS Flow Process</text>
  </g>

  <!-- entry marker -->
  <g class="entry-marker arrow-navy">
    <rect x="189" y="374" width="5" height="26"/>
    <polygon points="180,396 203,396 191.5,410"/>
    <rect x="178" y="413" width="28" height="4"/>
  </g>

  <!-- on-site hub -->
  <g class="hub hub-onsite">
    <path class="fan-back" d="M283,390 L249.7,245.8 A148 148 0 0 1 249.7,534.2 Z" filter="url(#soft-shadow)"/>
    <path class="sector-red" d="M258.7,252.1 A140 140 0 0 1 373,282.8 L331.2,332.6 A75 75 0 0 0 270,316.1 Z"/>
    <path class="sector-yellow" d="M373,282.8 A140 140 0 0 1 423,390 L358,390 A75 75 0 0 0 331.2,332.6 Z"/>
    <path class="sector-sky" d="M423,390 A140 140 0 0 1 373,497.2 L331.2,447.4 A75 75 0 0 0 358,390 Z"/>
    <path class="sector-green" d="M373,497.2 A140 140 0 0 1 258.7,527.9 L270,463.9 A75 75 0 0 0 331.2,447.4 Z"/>
    <path class="sector-core" d="M260.4,262 A130 130 0 0 1 366.6,290.4 L331.2,332.6 A75 75 0 0 0 270,316.1 Z"/>
    <path class="sector-core" d="M366.6,290.4 A130 130 0 0 1 413,390 L358,390 A75 75 0 0 0 331.2,332.6 Z"/>
    <path class="sector-core" d="M413,390 A130 130 0 0 1 366.6,489.6 L331.2,447.4 A75 75 0 0 0 358,390 Z"/>
    <path class="sector-core" d="M366.6,489.6 A130 130 0 0 1 260.4,518 L270,463.9 A75 75 0 0 0 331.2,447.4 Z"/>

    <text class="sector-label" text-anchor="middle" transform="translate(309.7,293.5) rotate(15)">Collect Worklist</text>
    <text class="sector-label" text-anchor="middle" transform="translate(373.3,346.5) rotate(65)">Scope Review</text>
    <text class="sector-label" text-anchor="middle" transform="translate(379.3,433.5) rotate(-65)">Planning Premise</text>
    <text class="sector-label" text-anchor="middle" transform="translate(309.7,492.5) rotate(-15)">Data Collection</text>

    <circle class="badge-ring" cx="337.7" cy="261.1" r="19" filter="url(#soft-shadow)"/>
    <use href="#ico-list" class="icon-navy" x="326.7" y="250.1" width="22" height="22"/>
    <circle class="badge-ring" cx="412.8" cy="337.6" r="19" filter="url(#soft-shadow)"/>
    <use href="#ico-scope" class="icon-navy" x="401.8" y="326.6" width="22" height="22"/>
    <circle class="badge-ring" cx="412.8" cy="442.4" r="19" filter="url(#soft-shadow)"/>
    <use href="#ico-scroll" class="icon-navy" x="401.8" y="431.4" width="22" height="22"/>
    <circle class="badge-ring" cx="337.7" cy="518.9" r="19" filter="url(#soft-shadow)"/>
    <use href="#ico-doc" class="icon-navy" x="326.7" y="507.9" width="22" height="22"/>

    <circle class="hub-halo" cx="283" cy="390" r="76" filter="url(#soft-shadow)"/>
    <circle cx="283" cy="390" r="60" fill="url(#disc-grad)"/>
    <use href="#ico-team" class="icon-navy" x="262" y="355" width="42" height="30"/>
    <text class="hub-label" x="283" y="417" text-anchor="middle">On Site</text>
  </g>

  <!-- arrow to field photos -->
  <g class="arrow-navy">
    <rect x="420" y="377" width="36" height="26"/>
    <polygon points="455,360 497,390 455,420"/>
  </g>

  <!-- field photos -->
  <g class="step step-photos">
    <polygon class="hex-outline-navy" points="505,391 545,320 625,320 665,391 625,462 545,462"/>
    <polygon class="hex-fill-navy" points="516,391 551,331 619,331 654,391 619,451 551,451"/>
    <circle class="hex-disc" cx="585" cy="391" r="40" fill="url(#disc-grad)"/>
    <use href="#ico-camera" class="icon-navy" x="566" y="376" width="38" height="30"/>
    <text class="step-label" x="585" y="489" text-anchor="middle">Field Photos</text>
  </g>

  <!-- arrow to remote -->
  <g class="arrow-navy">
    <rect x="654" y="377" width="38" height="26"/>
    <polygon points="691,360 735,390 691,420"/>
  </g>

  <!-- remote hub -->
  <g class="hub hub-remote">
    <path class="fan-back" d="M808,390 L833.7,244.3 A148 148 0 0 1 833.7,535.7 Z" filter="url(#soft-shadow)"/>
    <path class="sector-yellow" d="M844.2,254.8 A140 140 0 0 1 934.9,330.8 L876,358.3 A75 75 0 0 0 827.4,317.6 Z"/>
    <path class="sector-sky" d="M934.9,330.8 A140 140 0 0 1 934.9,449.2 L876,421.7 A75 75 0 0 0 876,358.3 Z"/>
    <path class="sector-green" d="M934.9,449.2 A140 140 0 0 1 844.2,525.2 L827.4,462.4 A75 75 0 0 0 876,421.7 Z"/>
    <path class="sector-core" d="M841.6,264.4 A130 130 0 0 1 925.8,335.1 L876,358.3 A75 75 0 0 0 827.4,317.6 Z"/>
    <path class="sector-core" d="M925.8,335.1 A130 130 0 0 1 925.8,444.9 L876,421.7 A75 75 0 0 0 876,358.3 Z"/>
    <path class="sector-core" d="M925.8,444.9 A130 130 0 0 1 841.6,515.6 L827.4,462.4 A75 75 0 0 0 876,421.7 Z"/>

    <text class="sector-label" text-anchor="middle" transform="translate(872,313.1) rotate(40)">Package Review</text>
    <text class="sector-label" text-anchor="middle" transform="translate(908,390) rotate(90)">Develop Package</text>
    <text class="sector-label" text-anchor="middle" transform="translate(876.2,470.9) rotate(-40)">Detail Planning</text>

    <circle class="badge-ring" cx="896.7" cy="284.3" r="19" filter="url(#soft-shadow)"/>
    <use href="#ico-cycle" class="icon-navy" x="885.7" y="273.3" width="22" height="22"/>
    <circle class="badge-ring" cx="945.8" cy="382.8" r="19" filter="url(#soft-shadow)"/>
    <use href="#ico-network" class="icon-navy" x="934.8" y="371.8" width="22" height="22"/>
    <circle class="badge-ring" cx="913.7" cy="478.7" r="19" filter="url(#soft-shadow)"/>
    <use href="#ico-window-search" class="icon-navy" x="902.7" y="467.7" width="22" height="22"/>

    <circle class="hub-halo" cx="808" cy="390" r="76" filter="url(#soft-shadow)"/>
    <circle cx="808" cy="390" r="60" fill="url(#disc-grad)"/>
    <use href="#ico-team" class="icon-navy" x="787" y="355" width="42" height="30"/>
    <text class="hub-label" x="808" y="406" text-anchor="middle">Remote</text>
    <use href="#ico-signal" class="icon-navy" x="796" y="415" width="24" height="16"/>
  </g>

  <!-- arrow down to acceptance -->
  <g class="arrow-navy">
    <rect x="910" y="514" width="20" height="28"/>
    <polygon points="897,540 943,540 920,563"/>
  </g>

  <!-- package acceptance -->
  <g class="step step-acceptance">
    <polygon class="hex-outline-navy" points="920,566 976,598 976,660 920,692 864,660 864,598"/>
    <polygon class="hex-fill-navy" points="920,577 966,604 966,654 920,681 874,654 874,604"/>
    <use href="#ico-handshake" class="icon-white" x="893" y="611" width="54" height="36"/>
    <text class="step-label" x="920" y="704" text-anchor="middle">Package Acceptance</text>
  </g>

  <!-- schedule chain -->
  <g class="arrow-navy">
    <polygon points="816,627 838,609 838,645"/>
    <rect x="837" y="618" width="22" height="18"/>
  </g>

  <g class="step step-level1">
    <polygon class="hex-outline-yellow" points="772,595 800,611 800,643 772,659 744,643 744,611"/>
    <polygon class="hex-fill-yellow" points="772,601 795,614 795,640 772,653 749,640 749,614"/>
    <circle cx="772" cy="627" r="16" fill="#fff"/>
    <use href="#ico-calendar" class="icon-navy" x="762" y="617" width="20" height="20"/>
    <text class="step-label" x="773" y="689" text-anchor="middle">Level 1</text>
  </g>
  <g class="arrow-yellow">
    <polygon points="705,627 727,609 727,645"/>
    <rect x="726" y="618" width="16" height="18"/>
  </g>

  <g class="step step-review-1">
    <polygon class="hex-outline-navy" points="660,595 688,611 688,643 660,659 632,643 632,611"/>
    <polygon class="hex-fill-navy" points="660,601 683,614 683,640 660,653 637,640 637,614"/>
    <circle cx="660" cy="627" r="16" fill="#fff"/>
    <use href="#ico-team" class="icon-navy" x="648" y="619" width="24" height="17"/>
    <text class="step-label" x="662" y="689" text-anchor="middle">Schedule Review</text>
  </g>
  <g class="arrow-navy">
    <polygon points="593,627 615,609 615,645"/>
    <rect x="614" y="618" width="16" height="18"/>
  </g>

  <g class="step step-level2">
    <polygon class="hex-outline-yellow" points="549,595 577,611 577,643 549,659 521,643 521,611"/>
    <polygon class="hex-fill-yellow" points="549,601 572,614 572,640 549,653 526,640 526,614"/>
    <circle cx="549" cy="627" r="16" fill="#fff"/>
    <use href="#ico-calendar" class="icon-navy" x="539" y="617" width="20" height="20"/>
    <text class="step-label" x="549" y="689" text-anchor="middle">Level 2</text>
  </g>
  <g class="arrow-yellow">
    <polygon points="482,627 504,609 504,645"/>
    <rect x="503" y="618" width="16" height="18"/>
  </g>

  <g class="step step-review-2">
    <polygon class="hex-outline-navy" points="437,595 465,611 465,643 437,659 409,643 409,611"/>
    <polygon class="hex-fill-navy" points="437,601 460,614 460,640 437,653 414,640 414,614"/>
    <circle cx="437" cy="627" r="16" fill="#fff"/>
    <use href="#ico-team" class="icon-navy" x="425" y="619" width="24" height="17"/>
    <text class="step-label" x="436" y="689" text-anchor="middle">Schedule Review</text>
  </g>
  <g class="arrow-navy">
    <polygon points="367,627 389,609 389,645"/>
    <rect x="388" y="618" width="17" height="18"/>
  </g>

  <g class="step step-level3">
    <circle class="hub-halo" cx="297" cy="628" r="60" filter="url(#soft-shadow)"/>
    <circle cx="297" cy="628" r="49" fill="url(#disc-grad)"/>
    <use href="#ico-calendar" class="icon-navy" x="284" y="597" width="26" height="26"/>
    <text class="small-hub-label" x="297" y="640" text-anchor="middle">Level 3 Schedule</text>
  </g>

  <!-- brand -->
  <text class="brand-mark" x="1232" y="692" text-anchor="middle">ZOL</text>
</svg>
</body>
</html>
```